KEV.PRO- Darren Holcombe Fitness- needs a clever business card using the logo, name, info, contact

I need a business card designed for my Online Personal Training company called KEV.PRO, abbreviation for Darren Holcombe Fitness. My company focuses on coaching in personal health and personal growth to unleash your greatest potential. I would like to see designs that use my color scheme of a redish-orange (C:0,M:84,Y:100,K:0), grey, white, black, and my company font is OSWALD. The final design should communicate some aspects of design, health, motivation, growth, in some way. The logo is very important to the company and can be displayed in any of the colors previously mentioned. Must include the company name, my website: www.kev-pro.example , my email: dan@kev-pro.example

Target Market(s)

Personal health, fitness, general public, those who lack knowledge, awareness, and confidence in personal health

Industry/Entity Type

Personal Trainer

Font styles to use
Other font styles liked:
• OSWALD. (Bold, Regular, Light)

Colors
f37122
ffffff
9d9d9d
000000

Requirements
Must have
• Must include the logo, company name, my website: www.kev-pro.example , my email: dan@kev-pro.example
Nice to have
• Variations of the colors scheme of a redish-orange (C:0,M:84,Y:100,K:0), grey, white, black. Logo, card, or text can be in any of these colors.
• Possible quote like "Take control of your personal health to unleash your greatest potential" or "Unleashing your greatness first begins with fitness of the body and mind"

```html
<!DOCTYPE html>
<html lang="en">
<head>
<meta charset="utf-8">
<title>KEV.PRO Business Card</title>
<link href="https://fonts.googleapis.com/css2?family=Oswald:wght@300;400;600;700&display=swap" rel="stylesheet">
<style>
  :root {
    --orange: #f04e23;
    --white: #ffffff;
    --grey-light: #a3a3a3;
    --grey-mid: #8f8f8f;
    --grey-dark: #5a5a5a;
    --card-black: #231f20;
    --ink: #1a1a1a;
    --backdrop: #efefef;
  }
  * { margin: 0; padding: 0; box-sizing: border-box; }
  html, body {
    width: 1200px;
    height: 1200px;
    overflow: hidden;
    background: var(--backdrop);
    font-family: "Oswald", sans-serif;
  }
  .canvas {
    position: relative;
    width: 1200px;
    height: 1200px;
    display: flex;
    align-items: center;
    justify-content: center;
    gap: 60px;
  }
  .card {
    position: relative;
    width: 380px;
    height: 665px;
    display: flex;
    flex-direction: column;
    align-items: center;
    text-align: center;
  }
  /* Front: grey card */
  .card--front {
    background: linear-gradient(160deg, var(--grey-dark) 0%, var(--grey-mid) 35%, var(--grey-light) 70%, var(--grey-light) 100%);
    padding-top: 120px;
  }
  .brand-mark {
    width: 150px;
    height: 150px;
    border-radius: 50%;
    border: 14px solid var(--orange);
  }
  .brand-name {
    margin-top: 22px;
    font-weight: 700;
    font-size: 50px;
    line-height: 1;
    color: var(--ink);
    letter-spacing: 0.5px;
  }
  .brand-sub {
    margin-top: 6px;
    font-weight: 300;
    font-size: 13px;
    color: var(--ink);
    text-transform: uppercase;
    letter-spacing: 0.3px;
  }
  .tagline {
    margin-top: 110px;
    font-weight: 600;
    font-size: 27px;
    line-height: 1.12;
    color: var(--orange);
    text-transform: uppercase;
  }
  /* Back: black card */
  .card--back {
    background: var(--card-black);
    padding-top: 85px;
  }
  .logo-ring {
    width: 270px;
    height: 270px;
    border-radius: 50%;
    border: 16px solid var(--orange);
    display: flex;
    align-items: center;
    justify-content: center;
  }
  .logo-ring .ring-name {
    font-weight: 700;
    font-size: 52px;
    color: var(--orange);
    letter-spacing: 0.5px;
  }
  .person-name {
    margin-top: 100px;
    font-weight: 600;
    font-size: 36px;
    line-height: 1;
    color: var(--white);
    text-transform: uppercase;
  }
  .person-role {
    margin-top: 2px;
    font-weight: 600;
    font-size: 24px;
    color: var(--white);
  }
  .contact {
    margin-top: 70px;
    list-style: none;
    font-weight: 400;
    font-size: 22px;
    line-height: 1.3;
    color: #e6e6e6;
  }
</style>
</head>
<body>
  <main class="canvas">
    <section class="card card--front" aria-label="Business card front">
      <div class="brand-mark" aria-hidden="true"></div>
      <h1 class="brand-name">KEV.PRO</h1>
      <p class="brand-sub">Darren Holcombe Fitness</p>
      <p class="tagline">Online<br>Personal Training<br>Company</p>
    </section>

    <section class="card card--back" aria-label="Business card back">
      <div class="logo-ring">
        <span class="ring-name">KEV.PRO</span>
      </div>
      <h2 class="person-name">Owen Tarrant</h2>
      <p class="person-role">Owner</p>
      <ul class="contact">
        <li>dan@kev-pro.example</li>
        <li>www.kev-pro.example</li>
      </ul>
    </section>
  </main>
</body>
</html>
```